R&t subterra

We specialize in CIPP pipe lining but do other underground utilities trenchless as well.

Target Market(s)

Trenchless sewer replacement

Contact Information for Business Card

Doug Falvey 715-482-6170 Pine Hollow, wi

```html
<!DOCTYPE html>
<html lang="en">
<head>
<meta charset="utf-8">
<title>R&amp;T Subterra – Business Card</title>
<link rel="stylesheet" href="https://fonts.googleapis.com/css2?family=Poppins:wght@400;500;600;700&display=swap">
<style>
  :root {
    --page-bg: #d9d1c5;
    --card-bg: #e6e0d6;
    --card-edge: #f3efe8;
    --brand-blue: #1f7ea6;
    --band-blue: #1b6f93;
    --name-grey: #6d6a66;
    --ink: #1c1c1c;
    --contact-tan: #d9b48c;
    --mark-grey: #8a857e;
  }
  * { margin: 0; padding: 0; box-sizing: border-box; }
  html, body {
    width: 1200px;
    height: 1046px;
    overflow: hidden;
    background: var(--page-bg);
    font-family: "Poppins", sans-serif;
  }
  .card {
    position: absolute;
    left: 80px;
    top: 240px;
    width: 1040px;
    height: 566px;
    background: var(--card-bg);
    border: 2px solid var(--card-edge);
    border-radius: 26px;
    overflow: hidden;
  }
  .brand {
    position: absolute;
    left: 40px;
    top: 70px;
    display: flex;
    align-items: center;
    gap: 18px;
  }
  .brand-dot {
    width: 70px;
    height: 70px;
    border-radius: 50%;
    background: var(--brand-blue);
  }
  .brand-name {
    font-weight: 700;
    font-size: 52px;
    color: var(--brand-blue);
    letter-spacing: 0.5px;
  }
  .person {
    position: absolute;
    right: 52px;
    top: 36px;
  }
  .person-name {
    font-size: 46px;
    line-height: 1.1;
    color: var(--name-grey);
    font-weight: 400;
  }
  .person-name .first {
    font-weight: 600;
    color: var(--brand-blue);
  }
  .person-role {
    font-size: 23px;
    font-weight: 500;
    color: var(--ink);
    margin-top: 2px;
  }
  .accent-bar {
    position: absolute;
    right: 0;
    top: 44px;
    width: 26px;
    height: 76px;
    background: var(--brand-blue);
  }
  .contact-band {
    position: absolute;
    left: 0;
    right: 0;
    bottom: 0;
    height: 128px;
    background: linear-gradient(90deg, #2a7896 0%, var(--band-blue) 55%, #175f80 100%);
    padding: 28px 0 0 36px;
  }
  .contact-line {
    display: flex;
    align-items: center;
    gap: 14px;
    font-size: 25px;
    color: var(--contact-tan);
    line-height: 34px;
  }
  .contact-line svg {
    width: 22px;
    height: 22px;
    flex: none;
  }
</style>
</head>
<body>
  <div class="card">
    <div class="brand">
      <div class="brand-dot"></div>
      <div class="brand-name">R&amp;T SUBTERRA</div>
    </div>

    <div class="person">
      <div class="person-name"><span class="first">Doug</span> Falvey</div>
      <div class="person-role">Sewer and Water Specialists</div>
    </div>
    <div class="accent-bar"></div>

    <div class="contact-band">
      <div class="contact-line">
        <svg viewBox="0 0 24 24" fill="none" stroke="#d9b48c" stroke-width="2" stroke-linecap="round" stroke-linejoin="round">
          <path d="M5 3h3l2 5-2.5 1.5a11 11 0 0 0 6 6L15 13l5 2v3a2 2 0 0 1-2 2A16 16 0 0 1 3 5a2 2 0 0 1 2-2z"/>
          <path d="M15 3a6 6 0 0 1 6 6M15 7a2 2 0 0 1 2 2"/>
        </svg>
        <span>715-482-6170</span>
      </div>
      <div class="contact-line">
        <svg viewBox="0 0 24 24" fill="none" stroke="#d9b48c" stroke-width="2" stroke-linecap="round" stroke-linejoin="round">
          <path d="M12 21s-6-6.2-6-11a6 6 0 0 1 12 0c0 4.8-6 11-6 11z"/>
          <circle cx="12" cy="10" r="2.2"/>
          <path d="M7 21h10"/>
        </svg>
        <span>Pine Hollow, wi</span>
      </div>
    </div>
  </div>
</body>
</html>
```